Flyer for the Radiant Harvest Worship Day 2020

I am looking to create a flyer for a one day prayer retreat our church is organizing.
This flyer will be posted on social media, websites and will also be printed so it can be mailed to people.
I am looking for something professional, with good use of our logo and band colors (logo colors).
I am counting on the designer's skill, creativity, art and knowledge of media communication to produce a flyer that will effectively and quickly convey the message we are trying to spread.
CONTENT OF THE FLYER:
Event title: Radiant Harvest Worship Day
Date: Tuesday July 2nd, 2020
Time: 11:00AM - 7:00PM
Maplewood Hotel, 4817 Birchfield Avenue, Portland, Maine 04109 (Room: Evergreen)
Event Key words to highlight what the event is about: Prayer, Sharing the Word, Panel discussion, prophecy, Impartation.
Key phrases:
A one day prayer retreat.
Jesus Chris is Lord
Contact info:
www.tolvex.org
Phone: 207 555 0143
Email: contact@brookmeadow.org

```html
<!DOCTYPE html>
<html lang="en">
<head>
<meta charset="utf-8">
<title>Radiant Harvest Worship Day 2020</title>
<link rel="stylesheet" href="https://fonts.googleapis.com/css2?family=Montserrat:wght@800&family=Jost:wght@500;700&family=Pinyon+Script&family=Cinzel:wght@500&family=Mulish:wght@500&display=swap">
<style>
  :root {
    --page: #ffffff;
    --ink: #0b0b0b;
    --white: #ffffff;
    --orange: #f39a1e;
    --script: #b9b9b9;
    --photo-warm: #4a3a30;
    --photo-mid: #2a2420;
  }
  * { margin: 0; padding: 0; box-sizing: border-box; }
  html, body { width: 1200px; height: 1200px; overflow: hidden; background: var(--page); }
  .flyer {
    position: absolute; left: 150px; top: 20px;
    width: 900px; height: 1160px;
    background: var(--ink); overflow: hidden;
    color: var(--white);
  }
  .block { position: absolute; left: 0; right: 0; text-align: center; white-space: nowrap; }
  .fade {
    background: linear-gradient(90deg, #d9d9d9 0%, #5a5a5a 100%);
    -webkit-background-clip: text; background-clip: text; color: transparent;
  }
  .title-top {
    top: 62px; font-family: "Montserrat", sans-serif; font-weight: 800;
    font-size: 68px; letter-spacing: 1px; line-height: 1;
  }
  .title-main {
    top: 130px; font-family: "Montserrat", sans-serif; font-weight: 800;
    font-size: 90px; line-height: 1; color: var(--orange); letter-spacing: 1px;
  }
  .tagline {
    top: 240px; font-family: "Mulish", sans-serif; font-weight: 500;
    font-size: 34px; letter-spacing: 9px; line-height: 1;
  }
  .tagline .fade { background: linear-gradient(90deg, #bdbdbd, #3a3a3a); -webkit-background-clip: text; background-clip: text; }
  .motto {
    top: 306px; font-family: "Pinyon Script", cursive; font-size: 54px;
    color: var(--script); line-height: 1;
  }
  .photo {
    position: absolute; left: 0; top: 390px; width: 900px; height: 380px;
    background: radial-gradient(ellipse 480px 230px at 450px 170px, var(--photo-warm) 0%, var(--photo-mid) 55%, var(--ink) 100%);
  }
  .day {
    top: 672px; font-family: "Jost", sans-serif; font-weight: 700;
    font-size: 46px; color: var(--orange); line-height: 1; letter-spacing: 1px;
  }
  .date {
    top: 716px; font-family: "Jost", sans-serif; font-weight: 700;
    font-size: 112px; line-height: 1; letter-spacing: 12px; padding-left: 12px;
  }
  .date span { background: linear-gradient(180deg, #ffffff 45%, #9a9a9a 100%); -webkit-background-clip: text; background-clip: text; color: transparent; }
  .time {
    top: 824px; font-family: "Jost", sans-serif; font-weight: 700;
    font-size: 44px; letter-spacing: 15px; padding-left: 15px; line-height: 1;
  }
  .venue {
    top: 880px; font-family: "Mulish", sans-serif; font-weight: 500;
    font-size: 16px; line-height: 1.3;
  }
  .brand {
    position: absolute; left: 70px; top: 985px;
    display: flex; align-items: center; gap: 12px;
  }
  .brand-dot { width: 22px; height: 22px; border-radius: 50%; background: var(--orange); }
  .brand-name { font-family: "Cinzel", serif; font-weight: 500; font-size: 44px; color: var(--white); line-height: 1; }
  .focus {
    position: absolute; left: 370px; top: 958px;
    display: grid; grid-template-columns: 287px 200px; row-gap: 10px;
    list-style: none; font-family: "Cinzel", serif; font-weight: 500; font-size: 22px;
  }
  .focus li { display: flex; align-items: center; gap: 8px; line-height: 1; }
  .focus svg { width: 13px; height: 20px; flex: none; }
  .contact {
    position: absolute; left: 68px; right: 40px; top: 1092px;
    display: flex; justify-content: space-between; align-items: center;
    font-family: "Cinzel", serif; font-weight: 500; font-size: 19px;
  }
  .contact-item { display: flex; align-items: center; gap: 12px; }
  .contact svg { width: 24px; height: 24px; flex: none; }
</style>
</head>
<body>
  <main class="flyer">
    <div class="photo" role="img" aria-label="Photo of hands clasped in prayer resting on an open Bible, lit softly against a dark background"></div>

    <div class="block title-top">RADIANT <span class="fade">HARVEST</span></div>
    <div class="block title-main">WORSHIP DAY</div>
    <div class="block tagline">A ONE DAY PRAYER <span class="fade">RETREAT.</span></div>
    <div class="block motto">Jesus Christ is Lord</div>

    <div class="block day">TUESDAY</div>
    <div class="block date"><span>07.02.20</span></div>
    <div class="block time">11:00AM-7:00PM</div>
    <div class="block venue">Evergreen Room Maplewood Hotel, 4817 Birchfield Avenue,<br>Portland, Maine 04109</div>

    <div class="brand">
      <span class="brand-dot"></span>
      <span class="brand-name">TOLVEX</span>
    </div>

    <ul class="focus">
      <li><svg viewBox="0 0 13 20"><path d="M5 0h3v5h5v3H8v12H5V8H0V5h5z" fill="#f39a1e"/></svg>Prayer</li>
      <li><svg viewBox="0 0 13 20"><path d="M5 0h3v5h5v3H8v12H5V8H0V5h5z" fill="#f39a1e"/></svg>Prophecy</li>
      <li><svg viewBox="0 0 13 20"><path d="M5 0h3v5h5v3H8v12H5V8H0V5h5z" fill="#f39a1e"/></svg>Sharing the Word</li>
      <li><svg viewBox="0 0 13 20"><path d="M5 0h3v5h5v3H8v12H5V8H0V5h5z" fill="#f39a1e"/></svg>Impartation</li>
      <li><svg viewBox="0 0 13 20"><path d="M5 0h3v5h5v3H8v12H5V8H0V5h5z" fill="#f39a1e"/></svg>Panel discussion</li>
    </ul>

    <div class="contact">
      <div class="contact-item">
        <svg viewBox="0 0 24 24"><circle cx="12" cy="12" r="10.5" fill="none" stroke="#f39a1e" stroke-width="2"/><path d="M8.5 6.5l2 2.5-1.2 1.4c.7 1.5 1.8 2.6 3.3 3.3l1.4-1.2 2.5 2-1.2 1.8c-3.8-.4-7.2-3.8-7.6-7.6z" fill="#f39a1e"/></svg>
        <span>207 555 0143</span>
      </div>
      <div class="contact-item">
        <svg viewBox="0 0 24 24"><rect x="2" y="5" width="20" height="14" rx="1" fill="#f39a1e"/><path d="M2.5 5.5L12 13l9.5-7.5" fill="none" stroke="#0b0b0b" stroke-width="1.6"/></svg>
        <span>contact@brookmeadow.org</span>
      </div>
      <div class="contact-item">
        <svg viewBox="0 0 24 24"><circle cx="12" cy="12" r="10" fill="none" stroke="#f39a1e" stroke-width="2"/><ellipse cx="12" cy="12" rx="4.5" ry="10" fill="none" stroke="#f39a1e" stroke-width="1.6"/><path d="M2 12h20M4 7h16M4 17h16" stroke="#f39a1e" stroke-width="1.6"/></svg>
        <span>www.tolvex.org</span>
      </div>
    </div>
  </main>
</body>
</html>
```